Kestrel Roofpower Company need Flier for Bureau of Fuel Planning

We need a 2 page flier for distributing to Military Contractors and Bureau of Fuel Planning. We install residential solar and this will be used for military base housing and other gov. projects on the residential home communities. We need to show how large of a company we are and how we are able to work with the military //gov. projects. Attached is our website and other marketing info for your use. Thanks and good luck!

Target Market(s)

Military and Government Contractors //Bureau of Fuel Planning

Industry/Entity Type

Solar Energy

Requirements
Must have
• Our Why - Statement included

```html
<!DOCTYPE html>
<html lang="en">
<head>
<meta charset="utf-8">
<title>Kestrel Roofpower – Government and Military Housing Flier</title>
<link href="https://fonts.googleapis.com/css2?family=Source+Sans+3:wght@400;600;700&family=Poppins:wght@400;600&display=swap" rel="stylesheet">
<style>
:root{
  --stage:#c8c8c8;
  --paper:#ffffff;
  --blue:#2b8fcf;
  --green:#9ccb3b;
  --ink:#6d7478;
  --soft:#eef0f0;
}
*{margin:0;padding:0;box-sizing:border-box}
html,body{width:1200px;height:1000px;overflow:hidden;background:var(--stage)}
body{position:relative;font-family:"Source Sans 3",Arial,sans-serif}
.page{position:absolute;top:95px;width:398px;height:811px;background:var(--paper);overflow:hidden;box-shadow:0 1px 3px rgba(0,0,0,.15)}
.page--front{left:142px}
.page--back{left:660px}
.abs{position:absolute}
.center{left:0;right:0;text-align:center}

/* brand */
.brand-mark{position:absolute;left:161px;top:22px;width:76px;height:76px;border:7px solid var(--blue);border-radius:50%}
.brand-name{position:absolute;left:0;right:0;top:105px;text-align:center;color:var(--blue);font-weight:600;font-size:23px;letter-spacing:.3px;line-height:1.1}

/* front */
.front-art{position:absolute;left:0;top:0}
.headline{top:428px;color:#fff;font-weight:700;font-size:24px;line-height:27px}
.subline{top:496px;color:#fff;font-size:18px;line-height:21px}
.perk{color:#fff;font-size:18px;display:flex;align-items:center}
.perk-badge{border:1.5px solid #fff;border-radius:50%;display:flex;align-items:center;justify-content:center;font-size:11px;line-height:1;text-align:center;margin-right:9px}
.perk--scale{left:80px;top:584px}
.perk--scale .perk-badge{width:30px;height:30px}
.perk--gov{left:46px;top:616px}
.perk--gov .perk-badge{width:38px;height:38px;font-size:10px}
.front-phone{top:665px;color:#fff;font-weight:700;font-size:24px;line-height:28px}
.front-web{top:693px;color:#fff;font-size:15px}
.offer{top:733px;color:#fff;font-size:18px;line-height:22px}
.offer strong{font-weight:400;font-size:21px}

/* back */
.intro{left:22px;width:192px;top:164px;text-align:center;color:var(--ink);font-size:11px;line-height:12.8px}
.intro p+p{margin-top:12px}
.intro b{color:var(--blue);font-weight:700}
.cost-chart{left:222px;top:168px}
.steps-title{top:295px;font-size:8px;color:var(--ink)}
.step{position:absolute;top:315px;width:80px;text-align:center;font-family:"Poppins",Arial,sans-serif}
.step svg{display:block;margin:0 auto}
.step-title{font-size:5.6px;font-weight:600;color:#333;line-height:10px;margin-top:4px}
.step-text{font-size:4.3px;color:var(--ink);line-height:10px;margin-top:3px}
.reviews{position:absolute;left:0;top:435px;width:398px;height:238px;background:var(--soft)}
.reviews-title{top:26px;color:var(--green);font-size:19px;font-weight:400}
.quote{color:var(--ink);font-size:11px;line-height:12.8px}
.quote-author{color:var(--green);font-weight:700;font-size:10px;margin-top:1px}
.quote--one{top:80px;left:70px;right:70px}
.quote--two{top:160px;left:70px;right:70px}
.contact{position:absolute;left:0;top:673px;width:398px;height:138px;background:var(--green);color:#fff;text-align:center}
.contact-label{padding-top:16px;font-size:17px;line-height:18px}
.contact-phone{font-weight:700;font-size:25px;line-height:26px}
.contact-address{font-size:13px;line-height:16px;margin-top:2px}
.contact-web{font-weight:700;font-size:21px;line-height:22px}
</style>
</head>
<body>

<!-- Front page -->
<section class="page page--front">
  <svg class="front-art" width="398" height="811" viewBox="0 0 398 811">
    <defs>
      <linearGradient id="houseTone" x1="0" y1="0" x2="0" y2="1">
        <stop offset="0" stop-color="#dfe6ea"/>
        <stop offset=".45" stop-color="#3d4548"/>
        <stop offset=".75" stop-color="#c9b28a"/>
        <stop offset="1" stop-color="#3f6a33"/>
      </linearGradient>
    </defs>
    <rect x="0" y="160" width="398" height="270" fill="url(#houseTone)" role="img" aria-label="Photo of a white two-storey family home at dusk with a roof fully covered in dark solar panels and warm lit windows"/>
    <polygon points="0,410 398,368 398,811 0,811" fill="var(--green)"/>
    <polygon points="0,427 398,400 398,705 0,735" fill="var(--blue)"/>
  </svg>

  <div class="brand-mark"></div>
  <div class="brand-name">KESTREL ROOFPOWER</div>

  <h1 class="abs center headline">Powering the Homes of<br>Those Who Serve.</h1>
  <p class="abs center subline">Solar for military base and<br>government housing</p>

  <div class="abs perk perk--scale"><span class="perk-badge">50k</span>50,000+ Homes Powered</div>
  <div class="abs perk perk--gov"><span class="perk-badge">gov<br>ready</span>Federal &amp; Military Ready</div>

  <p class="abs center front-phone">(800) 555-0142</p>
  <p class="abs center front-web">www.kestrelroofpower.com</p>

  <p class="abs center offer">Call today to Plan Your<br><strong>Base Housing Project</strong></p>
</section>

<!-- Back page -->
<section class="page page--back">
  <div class="brand-mark"></div>
  <div class="brand-name">KESTREL ROOFPOWER</div>

  <div class="abs intro">
    <p><b>Our Why:</b> the families who serve our country deserve homes that cost less to run and a cleaner planet to come home to. We build it with them.</p>
    <p>With 600+ installers across 22 states, we deliver community-scale projects on schedule and to federal standards.</p>
  </div>

  <svg class="abs cost-chart" width="170" height="112" viewBox="0 0 170 112" font-family="Source Sans 3, Arial, sans-serif">
    <text x="66" y="13" text-anchor="middle" font-size="15" font-weight="700" fill="var(--ink)">What Will My</text>
    <text x="66" y="30" text-anchor="middle" font-size="15" font-weight="700" fill="var(--ink)">Electricity Cost?</text>
    <path d="M3,71 L3,80 L126,80 L126,32 Q70,58 3,71 Z" fill="#7b8285"/>
    <text x="8" y="76" font-size="9" font-weight="700" fill="#fff" transform="rotate(-9 8 76)">Utility Bill Whitout Solar</text>
    <rect x="3" y="80" width="123" height="13" fill="var(--green)"/>
    <text x="13" y="90" font-size="9" font-weight="700" fill="#fff">Utility Bill With Solar</text>
    <text x="134" y="84" font-size="8" font-weight="700" fill="var(--ink)" transform="rotate(-90 134 84)">SAVINGS</text>
    <text x="3" y="106" font-size="10" font-weight="700" fill="var(--ink)">Year1</text>
    <text x="45" y="106" font-size="10" font-weight="700" fill="var(--ink)">Year10</text>
    <text x="93" y="106" font-size="10" font-weight="700" fill="var(--ink)">Year20</text>
  </svg>

  <p class="abs center steps-title">We Make It Easy</p>

  <svg class="abs" style="left:0;top:330px" width="398" height="30" viewBox="0 0 398 30">
    <g fill="none" stroke="#c5c9cb" stroke-width=".8" stroke-dasharray="2 2">
      <path d="M92,12 Q107,2 122,12"/>
      <path d="M182,12 Q197,2 212,12"/>
      <path d="M272,12 Q282,2 293,12"/>
    </g>
  </svg>

  <div class="step" style="left:22px">
    <svg width="54" height="54" viewBox="0 0 54 54">
      <circle cx="27" cy="27" r="24" fill="none" stroke="var(--blue)" stroke-width="3"/>
      <path d="M27,3 A24,24 0 0 1 51,27" fill="none" stroke="var(--green)" stroke-width="3"/>
      <rect x="18" y="19" width="18" height="13" rx="1.5" fill="none" stroke="var(--blue)" stroke-width="1.5"/>
      <circle cx="27" cy="24" r="2.5" fill="var(--blue)"/>
      <rect x="15" y="34" width="24" height="2" fill="var(--blue)"/>
      <circle cx="50" cy="23" r="3.5" fill="var(--green)"/>
    </svg>
    <p class="step-title">Speak To A Project<br>Consultant</p>
    <p class="step-text">Meet a consultant to review your project goals.</p>
  </div>

  <div class="step" style="left:112px">
    <svg width="54" height="54" viewBox="0 0 54 54">
      <circle cx="27" cy="27" r="24" fill="none" stroke="var(--blue)" stroke-width="3"/>
      <path d="M3,27 A24,24 0 0 1 27,3" fill="none" stroke="var(--green)" stroke-width="3"/>
      <rect x="16" y="17" width="20" height="16" fill="none" stroke="var(--blue)" stroke-width="1.5"/>
      <path d="M16,22 H36 M16,28 H36 M23,17 V33 M30,17 V33" stroke="var(--blue)" stroke-width="1"/>
      <circle cx="37" cy="16" r="3" fill="none" stroke="var(--green)" stroke-width="1.3"/>
      <path d="M26,33 V38 M21,38 H31" stroke="var(--blue)" stroke-width="1.5"/>
      <circle cx="27" cy="51" r="3.5" fill="var(--green)"/>
    </svg>
    <p class="step-title">We'll Design Your<br>Community System</p>
    <p class="step-text">We finalize every detail for federal specs.</p>
  </div>

  <div class="step" style="left:202px">
    <svg width="54" height="54" viewBox="0 0 54 54">
      <circle cx="27" cy="27" r="24" fill="none" stroke="var(--blue)" stroke-width="3"/>
      <path d="M27,51 A24,24 0 0 1 3,27" fill="none" stroke="var(--green)" stroke-width="3"/>
      <rect x="17" y="16" width="15" height="20" fill="none" stroke="var(--blue)" stroke-width="1.5"/>
      <path d="M20,21 H29 M20,25 H29 M20,29 H26" stroke="var(--blue)" stroke-width="1"/>
      <circle cx="33" cy="33" r="6" fill="#fff" stroke="var(--green)" stroke-width="1.5"/>
      <path d="M33,30 V33 H35.5" fill="none" stroke="var(--green)" stroke-width="1.2"/>
      <circle cx="4" cy="27" r="3.5" fill="var(--green)"/>
    </svg>
    <p class="step-title">Schedule Your Phased<br>Install</p>
    <p class="step-text">We phase installs around resident schedules.</p>
  </div>

  <div class="step" style="left:283px">
    <svg width="54" height="54" viewBox="0 0 54 54">
      <circle cx="27" cy="27" r="24" fill="none" stroke="var(--green)" stroke-width="3"/>
      <circle cx="27" cy="24" r="8" fill="none" stroke="var(--green)" stroke-width="1.5"/>
      <path d="M23,33 H31 M24,36 H30" stroke="var(--green)" stroke-width="1.5"/>
      <path d="M27,20 V28 M27,24 Q30,21 30,19" fill="none" stroke="var(--green)" stroke-width="1.2"/>
      <path d="M27,11 V13 M18,15 L19.5,16.5 M36,15 L34.5,16.5" stroke="var(--green)" stroke-width="1.2"/>
      <circle cx="27" cy="3" r="3.5" fill="var(--green)"/>
    </svg>
    <p class="step-title">Start Saving Across<br>Every Home</p>
    <p class="step-text">Watch bills drop across the whole community.</p>
  </div>

  <div class="reviews">
    <h2 class="abs center reviews-title">What Our Partners are Saying</h2>
    <blockquote class="abs center quote quote--one">
      We brought Kestrel in for 400 homes on base housing. They finished ahead of schedule and passed every inspection!
      <p class="quote-author">Dana R., Base Housing Office</p>
    </blockquote>
    <blockquote class="abs center quote quote--two">
      We had met with a few installers who couldn't handle the scale. Kestrel staffed the full community project and it's working great for residents.
      <p class="quote-author">MARCUS P., GENERAL CONTRACTOR</p>
    </blockquote>
  </div>

  <footer class="contact">
    <p class="contact-label">Contact Us:</p>
    <p class="contact-phone">(800) 555-0142</p>
    <p class="contact-address">118 Larkspur Ave., Suite 210-B, Fairhaven NJ 08099</p>
    <p class="contact-web">www.kestrelroofpower.com</p>
  </footer>
</section>

</body>
</html>
```